Flyer Vacation Gift Certificate

I need to create a beautiful flyer 8.5 x 11 PDF format flyer design. <br/><br/>Instructions:<br/>The flyer will really be a gift voucher for a las vegas vacation getaway. So must have a Las Vegas Theme exciting fun<br/><br/>The voucher should have two modules that will be editable. <br/>Must have a "Compliments Of" area and also must have an "Exclusively For" area<br/><br/>Keep in mind that this flyer will be printed so keep that in mind :)<br/><br/>Here the is the content for the vacation voucher:<br/><br/>There is no doubt that Las Vegas is one of the hottest travel destinations around the world. In fact, some people would even go as far as<br/>saying that perhaps it is THE hottest place to visit. Enjoy up to 4 nights of resort/casino accommodations in exciting Las Vegas, NV. Millions of people travel to this exciting city each year to enjoy its thrills. Thanks to the business you received this certificate from, now you can enjoy exciting Las Vegas, NV too!<br/><br/>Features:<br/>*Travel 7 Days A Week<br/>*Stay Your Choice Of Nights (1-4 Nights)<br/>*Good For Two Adults & Two Children<br/>*Pay Just The Taxes & Fees<br/>*Multiple Travel Date Requests Allowed<br/>*Fully Transferable To Another Person<br/>*Just A 30 Days Advance Notice Required<br/>*You Will Have 12 Months To Complete Travel After Redemption<br/><br/>HOW CAN WE DO THIS?<br/><br/>We contract with the world leading hotel chains and resorts to help them fill their otherwise empty rooms.<br/><br/>We help fill empty rooms which the hotels, resorts and cruise lines turn into additional revenue from other areas of their property and future bookings.<br/><br/>Hotels rarely experience full occupancy, yet they remain open, providing rooms and services at fixed costs. So when hotels give out their rooms by partnering with marketing companies like us, they might miss out on the room fee, but they already didn't have that in the first place, at least now they have the opportunity to gain a customer for their in-house restaurants, room service, their casinos, an extra day stay, future bookings, etc.<br/><br/>VIEW ALL THE DETAILS OF THIS SPECIAL OFFER AND REDEEM ONLINE AT <br/>WWW.TOPAZVOUCHERDESK.COM<br/><br/>Certificate ID # 47261-38504<br/>Expires 02/29/2020<br/><br/><br/>*terms and conditions apply see website for details<br/><br/>KEEP IN MIND THE EXAMPLES I AM UPLOADING ARE SIMPLY TO SHOW YOU THAT THEY CONTAIN THE "COMPLIMENTS OF" AND "EXCLUSIVELY FOR" ELEMENTS. THESE MUST BE INCLUDED IN NEW DESIGN. PLEASE ONLY USE THE CONTENT I PROVIDED IN BRIEF, DONT USE CONTENT FROM EXAMPLES.

Target Market(s)

CONSUMERS THAT HAVE BEEN REWARDED WITH A VACATION CERTIFICATE FOR DOING BUSINESS WITH A COMPANY.

COMPANIES USE THESE AS MARKETING INCENTIVES TO ATTRACT MORE CUSTOMERS AND TO REWARD LOYALTY, ETC.

Industry/Entity Type

Travel Industry

Colors

Designer to choose colors to be used in the design.

Requirements
Must have
• I need to create a beautiful flyer 8.5 x 11 PDF format flyer design.
• Instructions:
• The flyer will really be a gift voucher for a las vegas vacation getaway. So must have a Las Vegas Theme exciting fun
• The voucher should have two modules that will be editable.
• Must have a "Compliments Of" area and also must have an "Exclusively For" area
• Keep in mind that this flyer will be printed so keep that in mind :)
• Here the is the content for the vacation voucher:
• There is no doubt that Las Vegas is one of the hottest travel destinations around the world. In fact, some people would even go as far as
• saying that perhaps it is THE hottest place to visit. Enjoy up to 4 nights of resort/casino accommodations in exciting Las Vegas, NV. Millions of people travel to this exciting city each year to enjoy its thrills. Thanks to the business you received this certificate from, now you can enjoy exciting Las Vegas, NV too!
• Features:
• *Travel 7 Days A Week
• *Stay Your Choice Of Nights (1-4 Nights)
• *Good For Two Adults & Two Children
• *Pay Just The Taxes & Fees
• *Multiple Travel Date Requests Allowed
• *Fully Transferable To Another Person
• *Just A 30 Days Advance Notice Required
• *You Will Have 12 Months To Complete Travel After Redemption
• HOW CAN WE DO THIS?
• We contract with the world leading hotel chains and resorts to help them fill their otherwise empty rooms.
• We help fill empty rooms which the hotels, resorts and cruise lines turn into additional revenue from other areas of their property and future bookings.
• Hotels rarely experience full occupancy, yet they remain open, providing rooms and services at fixed costs. So when hotels give out their rooms by partnering with marketing companies like us, they might miss out on the room fee, but they already didn't have that in the first place, at least now they have the opportunity to gain a customer for their in-house restaurants, room service, their casinos, an extra day stay, future bookings, etc.
• VIEW ALL THE DETAILS OF THIS SPECIAL OFFER AND REDEEM ONLINE AT
• WWW.TOPAZVOUCHERDESK.COM
• Certificate ID # 47261-38504
• Expires 02/29/2020
• *terms and conditions apply see website for details
• KEEP IN MIND THE EXAMPLES I AM UPLOADING ARE SIMPLY TO SHOW YOU THAT THEY CONTAIN THE "COMPLIMENTS OF" AND "EXCLUSIVELY FOR" ELEMENTS. THESE MUST BE INCLUDED IN NEW DESIGN. PLEASE ONLY USE THE CONTENT I PROVIDED IN BRIEF, DONT USE CONTENT FROM EXAMPLES.
Nice to have
• EXCITING LAS VEGAS IMAGES THAT MAKE SOMEONE WANT TO GO THERE

```html
<!DOCTYPE html>
<html lang="en">
<head>
<meta charset="utf-8">
<title>Las Vegas Vacation Voucher</title>
<link rel="stylesheet" href="https://fonts.googleapis.com/css2?family=Exo+2:ital,wght@1,700;1,800;1,900&family=Quicksand:wght@500;600&display=swap">
<style>
  :root {
    --bg-top: #5b3620;
    --bg-mid: #a86b3a;
    --bg-low: #6a4128;
    --bg-bottom: #3a2217;
    --gold: #f0c880;
    --gold-deep: #d8a85c;
    --gold-text: #6b4525;
    --cream: #f7e3c4;
    --cream-bright: #fff4e0;
    --muted-gold: #c08a50;
    --sky: #5a86a8;
    --sky-deep: #2e4e6a;
    --tower: #c88a5a;
    --car: #e0457a;
  }
  * { box-sizing: border-box; margin: 0; padding: 0; }
  html, body { width: 927px; height: 1200px; overflow: hidden; }
  body { background: var(--bg-bottom); font-family: "Quicksand", sans-serif; }

  .voucher {
    position: relative;
    width: 927px;
    height: 1200px;
    overflow: hidden;
    background: linear-gradient(160deg, var(--bg-top) 0%, var(--bg-mid) 30%, var(--bg-low) 70%, var(--bg-bottom) 100%);
  }

  .compliments-disc {
    position: absolute;
    left: -120px; top: -170px;
    width: 415px; height: 395px;
    border-radius: 50%;
    background: radial-gradient(circle at 60% 55%, var(--gold) 0%, var(--gold-deep) 100%);
  }
  .compliments-label {
    position: absolute;
    left: 38px; top: 44px;
    font-family: "Exo 2", sans-serif;
    font-style: italic; font-weight: 900;
    font-size: 18px; line-height: 24px;
    letter-spacing: 0.5px;
    color: var(--gold-text);
    text-transform: uppercase;
  }

  .intro {
    position: absolute;
    left: 308px; top: 42px; width: 540px;
    font-size: 18px; line-height: 23px; font-weight: 500;
    color: var(--cream);
  }

  .city-scene {
    position: absolute;
    left: 0; top: 310px;
    width: 927px; height: 580px;
  }

  .headline {
    position: absolute;
    left: 270px; top: 150px;
    width: 560px;
    transform: rotate(-5deg);
    transform-origin: left top;
    font-family: "Exo 2", sans-serif;
    font-style: italic;
    color: var(--cream-bright);
    text-transform: uppercase;
  }
  .headline .lead { font-weight: 800; font-size: 24px; letter-spacing: 0.5px; }
  .headline .nights { font-weight: 900; font-size: 68px; line-height: 60px; margin-left: 6px; }
  .headline .stay { display: block; font-weight: 800; font-size: 26px; line-height: 30px; }
  .headline .city { display: block; font-weight: 900; font-size: 96px; line-height: 84px; letter-spacing: -1px; }
  .headline .state { font-weight: 800; font-size: 22px; vertical-align: bottom; margin-left: 4px; }

  .outro {
    position: absolute;
    left: 0; top: 904px; width: 927px;
    text-align: center;
    font-size: 18px; line-height: 23px; font-weight: 500;
    color: var(--cream);
  }

  .features {
    position: absolute;
    top: 993px;
    list-style: none;
    font-size: 16.5px; line-height: 20.6px; font-weight: 500;
    color: var(--cream);
  }
  .features li { padding-left: 13px; text-indent: -13px; }
  .features li::before { content: "• "; }
  .features-left { left: 62px; }
  .features-right { left: 486px; width: 400px; }

  .redeem {
    position: absolute;
    left: 60px; top: 1112px;
    font-size: 14px; line-height: 17px; font-weight: 600;
    color: var(--muted-gold);
  }
  .redeem .caps { text-transform: uppercase; }

  .exclusive-band { position: absolute; left: 0; top: 0; }
  .exclusive-label {
    position: absolute;
    left: 540px; top: 1162px;
    font-family: "Exo 2", sans-serif;
    font-style: italic; font-weight: 900;
    font-size: 16px; letter-spacing: 1px;
    color: var(--gold-text);
    text-transform: uppercase;
  }
</style>
</head>
<body>
<main class="voucher">

  <div class="compliments-disc"></div>
  <p class="compliments-label">This voucher is<br>compliments of</p>

  <p class="intro">There is no doubt that Las Vegas is one of the hottest travel destinations around the world. In fact, some people would even go as far as saying that perhaps it is THE hottest place to visit.</p>

  <svg class="city-scene" role="img" aria-label="Las Vegas Strip skyline with palm trees, a rollercoaster and a pink vintage convertible in the foreground" viewBox="0 0 927 580">
    <defs>
      <linearGradient id="sceneTone" x1="0" y1="0" x2="0" y2="1">
        <stop offset="0" stop-color="var(--sky)"/>
        <stop offset="0.35" stop-color="var(--tower)"/>
        <stop offset="0.7" stop-color="#6f7f68"/>
        <stop offset="1" stop-color="var(--car)" stop-opacity="0.85"/>
      </linearGradient>
    </defs>
    <path d="M0 40 L240 20 L520 -10 L830 20 L927 0 L927 480 L840 540 L300 575 L0 540 Z" fill="url(#sceneTone)" opacity="0.9"/>
  </svg>

  <h1 class="headline">
    <span class="lead">Enjoy up to</span><span class="nights">4 Nights</span>
    <span class="stay">of resort/casino accommodations</span>
    <span class="stay">in exciting</span>
    <span class="city">Las Vegas<span class="state">NV,</span></span>
  </h1>

  <p class="outro">Millions of people travel to this exciting city each year to enjoy its thrills.<br>Thanks to the business you received this certificate from,<br>now you can enjoy exciting Las Vegas, NV too!</p>

  <ul class="features features-left">
    <li>Travel 7 Days A Week</li>
    <li>Stay Your Choice Of Nights (1-4 Nights)</li>
    <li>Good For Two Adults &amp; Two Children</li>
    <li>Pay Just The Taxes &amp; Fees</li>
  </ul>
  <ul class="features features-right">
    <li>Multiple Travel Date Requests Allowed</li>
    <li>Fully Transferable To Another Person</li>
    <li>Just A 30 Days Advance Notice Required</li>
    <li>You Will Have 12 Months To Complete Travel After Redemption</li>
  </ul>

  <div class="redeem">
    <p class="caps">View all the details of this special offer<br>and redeem online at www.topazvoucherdesk.com</p>
    <p>Certificate ID # 47261-38504 &nbsp;&nbsp;|&nbsp;&nbsp;&nbsp; Expires 02/29/2020</p>
    <p>*terms and conditions apply see website for details</p>
  </div>

  <svg class="exclusive-band" width="927" height="1200" viewBox="0 0 927 1200" aria-hidden="true">
    <defs>
      <linearGradient id="bandGold" x1="0" y1="0" x2="1" y2="0">
        <stop offset="0" stop-color="#c9974f"/>
        <stop offset="0.5" stop-color="var(--gold)"/>
        <stop offset="1" stop-color="#d9aa62"/>
      </linearGradient>
    </defs>
    <line x1="434" y1="1006" x2="484" y2="1200" stroke="var(--gold-deep)" stroke-width="1"/>
    <polygon points="463,1117 927,1117 927,1200 484,1200" fill="url(#bandGold)"/>
  </svg>
  <p class="exclusive-label">Exclusively for:</p>

</main>
</body>
</html>
```